Business Card Design

Business sales of reconditioned / used batteries with mobile delivery and install services. Customers base majority are auto car sales lots and individuals.

Card need to convey quality product reliability and quick prompt professional service.

Card must reflect excellence in customer care and product being offered

Target Market(s)

Auto car lots new and used. Auto repair shops. Individuals.

Industry/Entity Type

Business

Contact Information for Business Card

Cells Q-Dash
Cars, Trucks, Boats, Motorcycles, lawn mowers, power tools
Delivery & install available most vehicles
Mon-Sat 9-6pm
Lyle Brockett 501-738-2054
*product warranty 6 month shelf life battery/1 year blems battery

```html
<!DOCTYPE html>
<html lang="en">
<head>
<meta charset="utf-8">
<title>Cells Q-Dash – Business Card</title>
<link href="https://fonts.googleapis.com/css2?family=Open+Sans:wght@300;400;700;800&display=swap" rel="stylesheet">
<style>
  :root {
    --page: #ffffff;
    --card-light: #ffffff;
    --card-dark: #000000;
    --ink: #111111;
    --white: #ffffff;
    --red: #e30613;
    --red-soft: #f08a6c;
  }
  * { margin: 0; padding: 0; box-sizing: border-box; }
  html, body {
    width: 1200px;
    height: 1000px;
    overflow: hidden;
    background: var(--page);
    font-family: "Open Sans", Arial, sans-serif;
  }
  .card {
    position: absolute;
    left: 47px;
    top: 195px;
    width: 1086px;
    height: 637px;
    background: var(--card-dark);
    box-shadow: 0 6px 14px rgba(0, 0, 0, 0.35);
    overflow: hidden;
  }
  .card-header {
    position: absolute;
    left: 0; top: 0;
    width: 100%;
    height: 217px;
    background: var(--card-light);
  }
  .brand-name {
    position: absolute;
    left: 0; right: 0;
    top: 72px;
    text-align: center;
    font-size: 66px;
    font-weight: 800;
    color: var(--ink);
    letter-spacing: 0.5px;
    line-height: 1;
  }
  .accent-band {
    position: absolute;
    left: 0; top: 194px;
    width: 100%;
    height: 23px;
    background: linear-gradient(90deg,
      rgba(255,255,255,0) 0%,
      rgba(255,255,255,0) 13%,
      var(--red-soft) 50%,
      var(--red) 88%,
      var(--red) 100%);
  }
  .service-list {
    position: absolute;
    left: 61px;
    top: 233px;
    list-style: none;
  }
  .service-list li {
    display: flex;
    align-items: center;
    height: 39.5px;
    font-size: 31px;
    font-weight: 400;
    color: var(--white);
    line-height: 1;
  }
  .service-list svg {
    width: 26px;
    height: 24px;
    margin-right: 12px;
    flex: none;
  }
  .warranty {
    position: absolute;
    left: 57px;
    top: 560px;
    font-size: 23.5px;
    color: var(--white);
    line-height: 1;
  }
  .contact {
    position: absolute;
    right: 60px;
    top: 298px;
    text-align: right;
    color: var(--white);
  }
  .contact-name {
    font-size: 43px;
    font-weight: 300;
    line-height: 1;
    letter-spacing: 0.5px;
  }
  .contact-phone {
    margin-top: 8px;
    font-size: 53px;
    font-weight: 700;
    line-height: 1;
  }
  .contact-hours {
    margin-top: 38px;
    font-size: 33px;
    font-weight: 400;
    line-height: 1;
  }
</style>
</head>
<body>
  <svg width="0" height="0" style="position:absolute">
    <defs>
      <symbol id="chevrons" viewBox="0 0 26 24">
        <polygon points="0,0 7,0 14,12 7,24 0,24 7,12" fill="#e30613"/>
        <polygon points="11,0 18,0 25,12 18,24 11,24 18,12" fill="#e30613"/>
      </symbol>
    </defs>
  </svg>

  <div class="card">
    <header class="card-header">
      <div class="brand-name">Cells Q-Dash</div>
      <div class="accent-band"></div>
    </header>

    <ul class="service-list">
      <li><svg><use href="#chevrons"/></svg>Cars</li>
      <li><svg><use href="#chevrons"/></svg>Trucks</li>
      <li><svg><use href="#chevrons"/></svg>Boats</li>
      <li><svg><use href="#chevrons"/></svg>Motorcycles</li>
      <li><svg><use href="#chevrons"/></svg>Lawn mowers</li>
      <li><svg><use href="#chevrons"/></svg>Power tools</li>
      <li><svg><use href="#chevrons"/></svg>Delivery &amp; Install available</li>
      <li><svg><use href="#chevrons"/></svg>Most vehicles</li>
    </ul>

    <p class="warranty">*product warranty 6 month shelf life battery/1 year blems battery</p>

    <div class="contact">
      <div class="contact-name">LYLE BROCKETT</div>
      <div class="contact-phone">501-738-2054</div>
      <div class="contact-hours">Monday-Saturday 9-6pm</div>
    </div>
  </div>
</body>
</html>
```